Business card design Needed for new logo / Construction business, home extensions and new builds

We need a business card design using our new logo files which i will attach to this project :)

We are a small construction business specialising in home extensions, new builds and property development. We are very ambitious and would appreciate professional and elegant designs for our new business card.

Very serious about using the services on BriefNest and recently acquired our new logo from here :)

Please get involved, i will feedback when i can as i am very busy but can respond daily, thanks

Target Market(s)

People that want to build onto their houses, new building developments or adding too their existing property

Industry/Entity Type

Construction

Contact Information for Business Card

Hollin Marsh Construction, Tobias Renwick (Managing Director), Tel 07822200444, email - info@hollin-marsh, www.hollin-marsh.co.uk

Colors

Designer to choose colors to be used in the design.

Requirements
Must have
• I like a deep grey on the back please. A lot of you have provided black from and back, try mixing things up a little. The black looks cool 😎 Thanks

```html
<!DOCTYPE html>
<html lang="en">
<head>
<meta charset="utf-8">
<title>Hollin Marsh Construction – Business Card</title>
<link rel="stylesheet" href="https://fonts.googleapis.com/css2?family=Cinzel:wght@500;600&family=Montserrat:wght@400;500&display=swap">
<style>
  :root {
    --bg: #1f1f1f;
    --card-grey: #676767;
    --gold: #d6a23a;
    --gold-edge: #c8902a;
    --silver: #d9d9d9;
    --white: #ffffff;
  }
  * { margin: 0; padding: 0; box-sizing: border-box; }
  html, body { width: 1200px; height: 987px; overflow: hidden; }
  body {
    background: var(--bg);
    display: flex;
    align-items: center;
    justify-content: center;
    gap: 48px;
    font-family: "Montserrat", sans-serif;
  }
  .card {
    position: relative;
    width: 540px;
    height: 309px;
    border-radius: 18px;
    border-bottom: 3px solid var(--gold-edge);
    border-right: 2px solid var(--gold-edge);
    background: var(--card-grey);
    overflow: hidden;
  }
  /* Back */
  .card-back .pattern-area {
    position: absolute;
    inset: 0;
    background: linear-gradient(135deg, #3f3f3f 0%, #626262 45%, #8a8a8a 100%);
  }
  .card-back .brand-mark {
    position: absolute;
    right: 40px;
    top: 132px;
    display: flex;
    align-items: center;
    gap: 7px;
    font-family: "Cinzel", serif;
    font-weight: 600;
    font-size: 13px;
    color: var(--gold);
    letter-spacing: 0.5px;
  }
  .brand-mark .dot { width: 8px; height: 8px; background: var(--gold); }
  /* Front */
  .card-front .brand {
    position: absolute;
    right: 34px;
    top: 44px;
    width: 210px;
    display: flex;
    align-items: center;
    gap: 10px;
    font-family: "Cinzel", serif;
    font-weight: 600;
    font-size: 18px;
    line-height: 1.25;
    color: var(--silver);
    letter-spacing: 0.5px;
  }
  .brand .dot { width: 12px; height: 12px; background: var(--silver); flex: none; }
  .card-front .person {
    position: absolute;
    left: 34px;
    top: 128px;
  }
  .person .name {
    font-family: "Cinzel", serif;
    font-weight: 600;
    font-size: 25px;
    color: var(--gold);
    line-height: 1.1;
  }
  .person .role {
    font-size: 15px;
    color: var(--white);
    margin-top: 3px;
  }
  .card-front .contacts {
    position: absolute;
    left: 34px;
    bottom: 28px;
    list-style: none;
    display: flex;
    flex-direction: column;
    gap: 8px;
  }
  .contacts li {
    display: flex;
    align-items: center;
    gap: 9px;
    font-size: 15px;
    color: var(--white);
  }
  .contacts svg { width: 14px; height: 14px; flex: none; }
</style>
</head>
<body>
  <section class="card card-back">
    <div class="pattern-area" role="img" aria-label="Repeating embossed brand pattern in graded greys"></div>
    <div class="brand-mark"><span class="dot"></span>Hollin Marsh Construction</div>
  </section>

  <section class="card card-front">
    <div class="brand"><span class="dot"></span><span>Hollin Marsh Construction</span></div>
    <div class="person">
      <p class="name">Tobias Renwick</p>
      <p class="role">Managing Director</p>
    </div>
    <ul class="contacts">
      <li>
        <svg viewBox="0 0 24 24" aria-hidden="true"><path fill="#d6a23a" d="M6.6 10.8a15.1 15.1 0 0 0 6.6 6.6l2.2-2.2c.3-.3.7-.4 1-.2 1.1.4 2.3.6 3.6.6.6 0 1 .4 1 1V20c0 .6-.4 1-1 1A17 17 0 0 1 3 4c0-.6.4-1 1-1h3.5c.6 0 1 .4 1 1 0 1.3.2 2.5.6 3.6.1.3 0 .7-.2 1z"/></svg>
        07822200444
      </li>
      <li>
        <svg viewBox="0 0 24 24" aria-hidden="true"><path fill="#d6a23a" d="M3 5h18v14H3z"/><path fill="none" stroke="#676767" stroke-width="1.8" d="M3 5l9 7 9-7"/></svg>
        info@hollin-marsh
      </li>
      <li>
        <svg viewBox="0 0 24 24" aria-hidden="true"><circle cx="12" cy="12" r="9" fill="#d6a23a"/><path fill="none" stroke="#676767" stroke-width="1.4" d="M3 12h18M12 3c3 3 3 15 0 18M12 3c-3 3-3 15 0 18"/></svg>
        www.hollin-marsh.co.uk
      </li>
    </ul>
  </section>
</body>
</html>
```